Reef Glow

sunglasses, sihoullette of body, maybe wearing a bikini or sunglasses. I am offering spray tanning, body wraps, tanning beds, stand up, body art, airbrush makeup.

Target Market(s)

I would say my target is all ages, But tanning is a seasonal business and more beauty and aging concept. and around prom time I get my most profitable business. so 18 to 21 through march and april. then 25 to 55 through april to june.

Industry/Entity Type

Makeup

Contact Information for Business Card

Phone number: 701-382-5147 Owner: Jan Mortby (Lisowski)

Colors

Designer to choose colors to be used in the design.

Requirements
Nice to have
• Sunglasses, silouttes of body wearing sunglasses or bikini, or picture of spray gun.

```html
<!DOCTYPE html>
<html lang="en">
<head>
<meta charset="utf-8">
<title>Jan Mortby Lisowski – Business Card</title>
<link rel="stylesheet" href="https://fonts.googleapis.com/css2?family=Cormorant+SC:wght@600&family=Cormorant+Garamond:wght@500&family=Alegreya+SC:ital,wght@1,800&display=swap">
<style>
  :root {
    --bg-light: #a2643f;
    --bg-mid: #8a4f2c;
    --bg-dark: #5f3119;
    --cream: #ffffff;
    --motif: rgba(232, 200, 170, 0.28);
    --shadow: rgba(40, 18, 6, 0.65);
  }
  html, body {
    margin: 0;
    padding: 0;
    width: 1200px;
    height: 702px;
    overflow: hidden;
    background: #ffffff;
  }
  .card {
    position: relative;
    width: 1200px;
    height: 702px;
    overflow: hidden;
    background: radial-gradient(ellipse at 35% 30%, var(--bg-light) 0%, var(--bg-mid) 55%, var(--bg-dark) 100%);
    color: var(--cream);
  }
  .motif {
    position: absolute;
    background: radial-gradient(ellipse at center, var(--motif) 0%, rgba(232,200,170,0.08) 70%, transparent 100%);
  }
  .motif--sunglasses { left: 0; top: 0; width: 670px; height: 280px; border-bottom-right-radius: 50% 60%; }
  .motif--stars { left: 166px; top: 354px; width: 420px; height: 188px; border-radius: 50%; }
  .name-first {
    position: absolute;
    right: 157px;
    top: 178px;
    margin: 0;
    font: 600 64px/1 "Cormorant SC", serif;
    letter-spacing: 1px;
    text-shadow: 2px 2px 4px var(--shadow);
  }
  .name-last {
    position: absolute;
    left: 716px;
    top: 272px;
    margin: 0;
    font: italic 800 70px/1 "Alegreya SC", serif;
    text-shadow: 2px 2px 4px var(--shadow);
  }
  .phones {
    position: absolute;
    left: 686px;
    top: 438px;
    display: flex;
    align-items: center;
    gap: 12px;
  }
  .phone-icon { width: 96px; height: 92px; }
  .phone-list {
    margin: 0;
    padding: 0;
    list-style: none;
    font: 500 36px/1.45 "Cormorant Garamond", serif;
    letter-spacing: 1px;
  }
  .services {
    position: absolute;
    left: 116px;
    top: 580px;
    margin: 0;
    font: 600 19.5px/1 "Cormorant SC", serif;
    letter-spacing: 0.6px;
    text-transform: lowercase;
    font-variant: small-caps;
  }
</style>
</head>
<body>
  <div class="card">
    <div class="motif motif--sunglasses" role="img" aria-label="Faint outline of sunglasses"></div>
    <div class="motif motif--stars" role="img" aria-label="Three faint decorative stars"></div>

    <h1 class="name-first">Jan Mortby</h1>
    <p class="name-last">Lisowski</p>

    <div class="phones">
      <svg class="phone-icon" viewBox="0 0 96 92" aria-hidden="true">
        <path fill="var(--cream)" d="M6 30 C6 10 90 10 90 30 L90 38 C90 42 87 44 83 44 L70 44 C66 44 64 41 64 37 L64 31 C54 27 42 27 32 31 L32 37 C32 41 30 44 26 44 L13 44 C9 44 6 42 6 38 Z"/>
        <path fill="var(--cream)" d="M30 36 L66 36 L82 62 L82 86 C82 89 80 91 77 91 L19 91 C16 91 14 89 14 86 L14 62 Z"/>
        <circle cx="48" cy="66" r="13" fill="var(--bg-mid)"/>
        <circle cx="48" cy="66" r="5" fill="var(--cream)"/>
      </svg>
      <ul class="phone-list">
        <li>(701) 382 5147</li>
        <li>(701) 555 0138</li>
      </ul>
    </div>

    <p class="services">Spray tanning, body wraps, tanning beds, stand up, body art, airbrush make up</p>
  </div>
</body>
</html>
```